Brivora Collective Business Card Design

We need a business card design for Brivora Collective. We are a healthcare recruiting, wellness and education company. We partner with medical facilities to find quality candidates. We also offer free wellness courses.
The final design should communicate an emphasis on recruiting and wellness
The main purpose of the business card is to utilized it for networking events, give to hospitals, executives, VCs surgery centers and clinics. I want it to be sleek, clean, use of our brand colors and professional.

```html
<!DOCTYPE html>
<html lang="en">
<head>
<meta charset="utf-8">
<title>Brivora Collective Business Card</title>
<link href="https://fonts.googleapis.com/css2?family=PT+Serif&family=Roboto:wght@400&display=swap" rel="stylesheet">
<style>
  :root {
    --page-bg: #8c8c8c;
    --card-white: #f3f3f3;
    --brand-teal: #0f5f56;
    --text-grey: #5e5e5e;
    --photo-light: #4f9990;
    --photo-dark: #2a6e66;
    --white: #ffffff;
  }
  * { margin: 0; padding: 0; box-sizing: border-box; }
  html, body { width: 1188px; height: 1200px; overflow: hidden; }
  body { background: var(--page-bg); position: relative; font-family: 'Roboto', sans-serif; }

  .card { position: absolute; left: 245px; width: 696px; height: 386px; overflow: hidden; }
  .card-front { top: 159px; background: var(--card-white); }
  .card-back { top: 627px; }

  .portrait {
    position: absolute; left: 55px; top: 60px; width: 66px; height: 66px;
    border-radius: 50%; border: 2px solid var(--brand-teal);
    background: radial-gradient(circle at 50% 40%, #e6c7a6 0%, #c89a73 45%, #b59ac4 100%);
  }
  .person-name {
    position: absolute; left: 138px; top: 62px;
    font-family: 'PT Serif', serif; font-size: 30px; color: var(--brand-teal); line-height: 1;
  }
  .person-title {
    position: absolute; left: 139px; top: 100px;
    font-size: 19px; color: var(--text-grey); line-height: 1;
  }
  .address {
    position: absolute; left: 139px; top: 200px;
    font-size: 17px; color: var(--text-grey); line-height: 22px; letter-spacing: 0.3px;
  }
  .contact-list { position: absolute; left: 139px; top: 255px; list-style: none; }
  .contact-list li {
    display: flex; align-items: center; gap: 6px;
    font-size: 17px; color: var(--text-grey); height: 24.5px; letter-spacing: 0.3px;
  }
  .contact-list svg { width: 18px; height: 18px; flex: none; }

  .brand-front {
    position: absolute; left: 434px; top: 262px;
    display: flex; align-items: center; gap: 12px;
  }
  .brand-mark { width: 34px; height: 34px; background: var(--brand-teal); border-radius: 5px; }
  .brand-name {
    font-family: 'PT Serif', serif; color: var(--brand-teal);
    font-size: 28px; line-height: 30px;
  }

  .backdrop-photo {
    position: absolute; inset: 0;
    background: linear-gradient(100deg, var(--photo-dark) 0%, var(--photo-light) 45%, #5aa198 70%, var(--photo-dark) 100%);
  }
  .brand-back {
    position: absolute; left: 48px; top: 46px;
    display: flex; flex-direction: column; align-items: center; gap: 14px; width: 170px;
  }
  .brand-back .brand-mark { width: 56px; height: 56px; background: var(--white); border-radius: 8px; }
  .brand-back .brand-name { color: var(--white); font-size: 32px; line-height: 34px; text-align: center; }
  .tagline {
    position: absolute; left: 255px; top: 225px;
    font-family: 'PT Serif', serif; color: var(--white);
    font-size: 31px; line-height: 39px;
  }
</style>
</head>
<body>

<section class="card card-front">
  <div class="portrait" role="img" aria-label="Portrait photo of the founder"></div>
  <h1 class="person-name">Marina Holt</h1>
  <p class="person-title">Founder &amp; CEO</p>

  <p class="address">48 Elm Avenue, Suite 4<br>Lakeford, MA 01990</p>

  <ul class="contact-list">
    <li>
      <svg viewBox="0 0 24 24"><path fill="#0f5f56" d="M6.6 10.8a15 15 0 0 0 6.6 6.6l2.2-2.2c.3-.3.7-.4 1-.2 1.1.4 2.3.6 3.6.6.6 0 1 .4 1 1V20c0 .6-.4 1-1 1C10.6 21 3 13.4 3 4c0-.6.4-1 1-1h3.5c.6 0 1 .4 1 1 0 1.3.2 2.5.6 3.6.1.3 0 .7-.2 1z"/></svg>
      (555) 418-2093
    </li>
    <li>
      <svg viewBox="0 0 24 24"><rect x="2" y="5" width="20" height="14" fill="none" stroke="#0f5f56" stroke-width="2"/><path d="M2 5l10 8 10-8M2 19l7-7M22 19l-7-7" fill="none" stroke="#0f5f56" stroke-width="2"/></svg>
      info@brivoracollective.com
    </li>
    <li>
      <svg viewBox="0 0 24 24"><g fill="none" stroke="#0f5f56" stroke-width="1.6"><circle cx="12" cy="12" r="9.5"/><ellipse cx="12" cy="12" rx="4" ry="9.5"/><path d="M2.5 12h19M4 7h16M4 17h16"/></g></svg>
      www.brivoracollective.com
    </li>
  </ul>

  <div class="brand-front">
    <span class="brand-mark"></span>
    <span class="brand-name">Brivora<br>Collective</span>
  </div>
</section>

<section class="card card-back">
  <div class="backdrop-photo" role="img" aria-label="Teal-tinted photo of doctors and staff walking through a bright hospital lobby"></div>
  <div class="brand-back">
    <span class="brand-mark"></span>
    <span class="brand-name">Brivora<br>Collective</span>
  </div>
  <p class="tagline">Transforming<br>the healthcare employment<br>experience</p>
</section>

</body>
</html>
```